Inspiring Fundraising Foundation Website to Provide Academic Scholarships

Hello, we are launching a foundation to provide academic scholarships to high school students for college. We'd like this to be an informational website with contact information. There will be a total of approximately 5-7 pages in all.
The color scheme will be purple and white, with a girly feel. I 've attached the logo for reference!

Reason: Extending deadline to go over revisions

Target Market(s)

high school students, college students

Industry/Entity Type

Education

Coding

Coded - Design and coding required

Number of Pages Required

5+ page

Font styles to use
Serif
Sans Serif
Script

Colors
6b449b
886aae
b7a5cd
e4daeb
ffffff
fdf9cf
fbf289

Requirements
Must have
• Purple, girly feel, to reflect the logo's style. Should be light-themed
Should not have
• No dark themes (aka heavy on black or dark colors)

```html
<!DOCTYPE html>
<html lang="en">
<head>
<meta charset="utf-8">
<title>Rosalind Avery Foundation</title>
<link href="https://fonts.googleapis.com/css2?family=Open+Sans:wght@400;600;700&family=Raleway:wght@500;600;700&display=swap" rel="stylesheet">
<style>
:root{
  --purple:#6b449b;
  --purple-mid:#886aae;
  --purple-soft:#b7a5cd;
  --lavender:#e4daeb;
  --white:#ffffff;
  --cream:#fdf9cf;
  --yellow:#fbf289;
  --ink:#444;
  --muted:#888;
  --panel:#f2f2f2;
  --dark:#2f2f2f;
}
*{box-sizing:border-box;margin:0;padding:0}
html,body{width:1200px;height:2348px;overflow:hidden}
body{background:var(--white);font-family:"Open Sans",Arial,sans-serif;color:var(--ink);font-size:12px;line-height:1.6}
.wrap{width:940px;margin:0 auto;position:relative}
h1,h2,h3,h4{font-family:"Raleway",Arial,sans-serif;font-weight:600}

/* header */
.site-header{height:208px;position:relative}
.brand{position:absolute;left:0;top:28px;display:flex;align-items:center;gap:14px}
.brand-dot{width:52px;height:52px;border-radius:50%;background:var(--purple)}
.brand-name{font-family:"Raleway",Arial,sans-serif;font-weight:700;color:var(--purple);font-size:30px;line-height:1.05}
.contact-phone{position:absolute;right:0;top:30px;display:flex;align-items:center;gap:8px;color:var(--purple);font-family:"Raleway",sans-serif;font-weight:700;font-size:24px}
.search{position:absolute;right:0;top:78px;width:200px;height:30px;border:1px solid #ccc;border-radius:3px;display:flex;align-items:center;justify-content:flex-end;padding-right:8px}
.main-nav{position:absolute;right:0;top:160px;display:flex;gap:26px}
.main-nav a{font-family:"Raleway",sans-serif;font-size:11px;font-weight:600;color:#555;text-decoration:none;letter-spacing:.5px;padding-bottom:8px}
.main-nav a.active{color:var(--purple);border-bottom:2px solid var(--purple)}

/* hero */
.hero{height:400px;position:relative;background:linear-gradient(120deg,#c9b9a6 0%,#e8d6c2 30%,#b64d4b 55%,#d9c7b6 75%,#8c7a6b 100%)}
.hero-arrow{position:absolute;top:182px;width:36px;height:36px;border-radius:50%;background:rgba(255,255,255,.7);display:flex;align-items:center;justify-content:center}
.hero-arrow.prev{left:16px}.hero-arrow.next{right:16px}

/* welcome */
.welcome{height:252px;background:var(--purple);color:var(--white);text-align:center;position:relative}
.welcome h1{font-size:30px;padding-top:20px}
.welcome p{width:1000px;margin:14px auto 0;font-size:11.5px;line-height:1.75;color:#eadff3}
.founder{position:absolute;left:564px;top:212px;width:72px;height:72px;border-radius:50%;border:4px solid var(--white);background:linear-gradient(160deg,var(--purple-soft),var(--lavender));z-index:2}

/* mission */
.mission{height:380px;background:var(--lavender);padding-top:0}
.mission-box{width:900px;margin:0 auto;height:340px;background:var(--yellow);text-align:center;padding-top:56px}
.mission-box h2{font-size:27px;color:#333}
.pillars{display:flex;justify-content:space-between;padding:26px 60px 0}
.pillar{width:230px}
.pillar h3{font-size:19px;color:#333;margin:6px 0 4px}
.pillar p{font-size:10.5px;color:#6a6a50;line-height:1.6}
.btn{display:inline-block;margin-top:14px;padding:5px 20px;border:1px solid var(--purple-mid);background:var(--white);color:var(--purple);font-size:10.5px;border-radius:2px}

/* news */
.section-head{display:flex;justify-content:space-between;align-items:center;border-bottom:1px solid #ddd;padding-bottom:10px}
.section-head h2{font-size:27px;color:var(--purple)}
.view-all{padding:4px 12px;background:#999;color:var(--white);font-size:10px;border-radius:2px}
.news{height:340px;padding-top:40px}
.news-grid{display:flex;gap:16px;margin-top:22px}
.news-card{flex:1;height:200px;background:#f4f4f4;border-top:4px solid var(--purple);padding:18px 16px}
.news-card p{font-size:11px;color:#666}
.date{display:flex;align-items:center;gap:6px;margin-top:24px;font-size:10.5px;color:var(--muted)}

/* blog */
.blog{height:470px;background:var(--panel);padding-top:40px}
.blog-grid{display:flex;gap:22px;margin-top:30px}
.post{flex:1}
.post-img{height:150px}
.post h3{font-family:"Open Sans",sans-serif;font-size:12.5px;font-weight:700;color:var(--purple);margin-top:12px;line-height:1.35}
.post .date{margin-top:6px}
.post p{font-size:10.5px;color:#777;margin-top:6px}

/* footer */
.site-footer{position:absolute;left:0;top:2070px;width:1200px;height:226px;background:#efedf1}
.footer-cols{display:flex;gap:30px;padding-top:30px}
.footer-about{width:300px}
.footer-about h4{font-size:22px;color:#444;margin-bottom:8px}
.footer-about p{font-size:10.5px;color:#777}
.footer-col{flex:1;text-align:center}
.footer-icon{width:40px;height:40px;border-radius:50%;background:var(--purple);margin:0 auto 10px;display:flex;align-items:center;justify-content:center}
.footer-col h5{font-size:12px;color:#444;font-weight:700}
.footer-col li{list-style:none;font-size:10.5px;color:#777}
.socials{display:flex;gap:6px;justify-content:center;margin-top:4px}
.socials span{width:20px;height:20px;border-radius:50%}
.bottom-bar{position:absolute;left:0;top:2296px;width:1200px;height:52px;background:var(--dark);text-align:center;color:#aaa;font-size:10px;padding-top:9px}
.bottom-bar nav{display:flex;justify-content:center;gap:10px}
.bottom-bar nav a{color:#ccc;text-decoration:none}
</style>
</head>
<body>

<header class="site-header wrap">
  <div class="brand"><span class="brand-dot"></span><div class="brand-name">Rosalind Avery<br>Foundation</div></div>
  <div class="contact-phone">
    <svg width="20" height="20" viewBox="0 0 24 24"><path fill="#6b449b" d="M6.6 10.8a15 15 0 0 0 6.6 6.6l2.2-2.2c.3-.3.7-.4 1-.2 1.1.4 2.3.6 3.6.6.6 0 1 .4 1 1V20c0 .6-.4 1-1 1A17 17 0 0 1 3 4c0-.6.4-1 1-1h3.5c.6 0 1 .4 1 1 0 1.3.2 2.5.6 3.6.1.3 0 .7-.2 1z"/></svg>
    555.010.2468
  </div>
  <div class="search"><svg width="14" height="14" viewBox="0 0 24 24"><circle cx="10" cy="10" r="6" fill="none" stroke="#999" stroke-width="2"/><path d="M15 15l5 5" stroke="#999" stroke-width="2"/></svg></div>
  <nav class="main-nav">
    <a class="active" href="#">HOME</a><a href="#">ABOUT US</a><a href="#">SCHOLARSHIPS</a><a href="#">MEMBERSHIP</a><a href="#">NEWS &amp; EVENTS</a><a href="#">FUNDRAISING</a><a href="#">BLOG</a><a href="#">CONTACT US</a>
  </nav>
</header>

<section class="hero" role="img" aria-label="Photo of young students working together in a classroom">
  <span class="hero-arrow prev"><svg width="14" height="14" viewBox="0 0 24 24"><path d="M15 4l-8 8 8 8" fill="none" stroke="#555" stroke-width="3"/></svg></span>
  <span class="hero-arrow next"><svg width="14" height="14" viewBox="0 0 24 24"><path d="M9 4l8 8-8 8" fill="none" stroke="#555" stroke-width="3"/></svg></span>
</section>

<section class="welcome">
  <h1>Welcome to Rosalind Avery Foundation</h1>
  <p>Our foundation believes that every student deserves the chance to reach college. We partner with families, schools and local donors to open doors for young people who work hard and dream big. Each year we review applications from high school seniors across our region and award scholarships that cover tuition, books and the costs that often stand in the way. Beyond funding, we offer mentoring, campus visits and guidance through every step of the application process, so each scholar feels supported from the first form to the first day of class. Together we can build a brighter future, one student at a time.</p>
  <div class="founder" role="img" aria-label="Portrait of the foundation founder"></div>
</section>

<section class="mission">
  <div class="mission-box">
    <h2>We provide academic scholarships to high school students for college.</h2>
    <div class="pillars">
      <div class="pillar">
        <svg width="30" height="30" viewBox="0 0 24 24"><path d="M4 20h4L19 9l-4-4L4 16z" fill="none" stroke="#444" stroke-width="1.8"/><path d="M13 7l4 4" stroke="#444" stroke-width="1.8"/></svg>
        <h3>Apply for Scholarship</h3>
        <p>Submit your application online before the spring deadline and share your goals and story with us.</p>
        <span class="btn">Apply Now</span>
      </div>
      <div class="pillar">
        <svg width="30" height="30" viewBox="0 0 24 24"><circle cx="9" cy="8" r="3.5" fill="none" stroke="#444" stroke-width="1.8"/><circle cx="17" cy="9" r="2.5" fill="none" stroke="#444" stroke-width="1.8"/><path d="M2 20c0-4 3-6 7-6s7 2 7 6M15 14c4 0 7 2 7 5" fill="none" stroke="#444" stroke-width="1.8"/></svg>
        <h3>Join with us</h3>
        <p>Become a member and help guide the next class of scholars as a mentor, donor or volunteer.</p>
        <span class="btn">Register Now</span>
      </div>
      <div class="pillar">
        <svg width="30" height="30" viewBox="0 0 24 24"><circle cx="12" cy="12" r="9" fill="none" stroke="#444" stroke-width="1.8"/><path d="M15 8.5c-.8-.8-5-1.4-5 1.2 0 2.6 5 1.4 5 4.2 0 2.5-4.3 2-5.4 1.1M12 6v12" fill="none" stroke="#444" stroke-width="1.6"/></svg>
        <h3>Fundraising</h3>
        <p>Support our events and campaigns so that more students can afford the college of their dreams.</p>
        <span class="btn">Get Started</span>
      </div>
    </div>
  </div>
</section>

<section class="news wrap">
  <div class="section-head"><h2>News &amp; Events</h2><span class="view-all">View All</span></div>
  <div class="news-grid">
    <article class="news-card"><p>Spring scholarship applications are now open for seniors across the district this year.</p><div class="date"><svg width="12" height="12" viewBox="0 0 24 24"><rect x="3" y="5" width="18" height="16" fill="none" stroke="#888" stroke-width="2"/><path d="M3 10h18" stroke="#888" stroke-width="2"/></svg>17 February, 2017</div></article>
    <article class="news-card"><p>Join our annual gala dinner and help raise funds for the next class of scholars.</p><div class="date"><svg width="12" height="12" viewBox="0 0 24 24"><rect x="3" y="5" width="18" height="16" fill="none" stroke="#888" stroke-width="2"/><path d="M3 10h18" stroke="#888" stroke-width="2"/></svg>17 February, 2017</div></article>
    <article class="news-card"><p>Meet the mentors who volunteer their time to guide students through college planning.</p><div class="date"><svg width="12" height="12" viewBox="0 0 24 24"><rect x="3" y="5" width="18" height="16" fill="none" stroke="#888" stroke-width="2"/><path d="M3 10h18" stroke="#888" stroke-width="2"/></svg>17 February, 2017</div></article>
    <article class="news-card"><p>Campus visit day brings thirty high school students to tour local universities together.</p><div class="date"><svg width="12" height="12" viewBox="0 0 24 24"><rect x="3" y="5" width="18" height="16" fill="none" stroke="#888" stroke-width="2"/><path d="M3 10h18" stroke="#888" stroke-width="2"/></svg>17 February, 2017</div></article>
  </div>
</section>

<section class="blog">
  <div class="wrap">
    <div class="section-head"><h2>Blog</h2><span class="view-all">View All</span></div>
    <div class="blog-grid">
      <article class="post">
        <div class="post-img" role="img" aria-label="Photo of a student studying with books" style="background:linear-gradient(135deg,#8fa0b4,#d7dde3)"></div>
        <h3>Five tips for writing a scholarship essay that truly stands out</h3>
        <div class="date">17 February, 2017</div>
        <p>Your essay is a chance to share who you are. Start early, be honest, and let your own voice guide every paragraph you write.</p>
      </article>
      <article class="post">
        <div class="post-img" role="img" aria-label="Photo of graduates celebrating outdoors" style="background:linear-gradient(135deg,#a9b98e,#e6dfc6)"></div>
        <h3>How our first scholars are thriving during their college years</h3>
        <div class="date">17 February, 2017</div>
        <p>We caught up with last year's recipients to hear about classes, new friends and the lessons they learned in their first semester.</p>
      </article>
      <article class="post">
        <div class="post-img" role="img" aria-label="Photo of a classroom with students at desks" style="background:linear-gradient(135deg,#c79a6b,#e9d8c0)"></div>
        <h3>Planning ahead: a simple timeline for college applications</h3>
        <div class="date">17 February, 2017</div>
        <p>From junior year testing to senior year deadlines, this guide walks families through each step of the college journey.</p>
      </article>
    </div>
  </div>
</section>

<footer class="site-footer">
  <div class="wrap footer-cols">
    <div class="footer-about">
      <h4>About Us</h4>
      <p>We are a community foundation helping high school students reach college through scholarships, mentoring and guidance for every family we serve.</p>
    </div>
    <div class="footer-col">
      <div class="footer-icon"><svg width="18" height="18" viewBox="0 0 24 24"><path d="M4 20h4L19 9l-4-4L4 16z" fill="#fff"/></svg></div>
      <h5>Want more?</h5>
      <ul><li>Membership</li><li>Events</li><li>Login</li></ul>
    </div>
    <div class="footer-col">
      <div class="footer-icon"><svg width="18" height="18" viewBox="0 0 24 24"><path fill="#fff" d="M6.6 10.8a15 15 0 0 0 6.6 6.6l2.2-2.2c.3-.3.7-.4 1-.2 1.1.4 2.3.6 3.6.6.6 0 1 .4 1 1V20c0 .6-.4 1-1 1A17 17 0 0 1 3 4c0-.6.4-1 1-1h3.5c.6 0 1 .4 1 1 0 1.3.2 2.5.6 3.6.1.3 0 .7-.2 1z"/></svg></div>
      <h5>Talk to us</h5>
      <ul><li>555.010.2468</li><li>hello@averyfoundation.org</li></ul>
    </div>
    <div class="footer-col">
      <div class="footer-icon"><svg width="18" height="18" viewBox="0 0 24 24"><circle cx="6" cy="12" r="3" fill="#fff"/><circle cx="18" cy="6" r="3" fill="#fff"/><circle cx="18" cy="18" r="3" fill="#fff"/><path d="M6 12L18 6M6 12l12 6" stroke="#fff" stroke-width="2"/></svg></div>
      <h5>Stay in touch</h5>
      <div class="socials"><span style="background:#3b5998"></span><span style="background:#1da1f2"></span><span style="background:#6b449b"></span><span style="background:#dd4b39"></span></div>
    </div>
  </div>
</footer>

<div class="bottom-bar">
  <nav><a href="#">Home</a>|<a href="#">About Us</a>|<a href="#">Scholarships</a>|<a href="#">Membership</a>|<a href="#">News &amp; Events</a>|<a href="#">Fundraising</a>|<a href="#">Blog</a>|<a href="#">Contact Us</a></nav>
  <div>Copyright © 2017 - Rosalind Avery Foundation</div>
</div>

</body>
</html>
```